Medical Cannabis company is looking for a LOGO design *

SILVER MERIDIAN (SM) is a new company in the Israeli medical cannabis industry. We will engage in PREMIUM medical cannabis growing and cultivation and also manufacturing of HIGH-END cannabis based medical products.
the design should reflect luxury, high-end and Pharma-grade products.
the design should use color GOLD and NOT using the famous cannabis leaf !

Target Market(s)

international medical cannabis Pharmaceutical companies
and of course local and international patients

Contact Information for Business Card

Ron Ben-Amit
Founder and CEO

Silver Meridian
Medical grade cannabis

ronbenamit@mailpost-example.com
972-52-3186407

Colors
ffc214
fbed22

Requirements
Must have
• clean and simple
• luxury
• gold !!
• (can also have green for Cannabis and/or blue for Pharma)
Should not have
• cannabis leaf

```html
<!DOCTYPE html>
<html lang="en">
<head>
<meta charset="utf-8">
<title>Silver Meridian — Business Card</title>
<link rel="stylesheet" href="https://fonts.googleapis.com/css2?family=Tinos:wght@400;700&display=swap">
<style>
  :root {
    --backdrop: #1c1c1e;
    --card: #0b0b0c;
    --card-edge: #202022;
    --gold: #ecb91c;
    --gold-soft: #d9a81a;
  }
  * { box-sizing: border-box; margin: 0; padding: 0; }
  html, body {
    width: 1200px;
    height: 1200px;
    overflow: hidden;
    background: var(--backdrop);
  }
  .canvas {
    width: 1200px;
    height: 1200px;
    display: flex;
    flex-direction: column;
    align-items: center;
    justify-content: center;
    gap: 60px;
  }
  .card {
    width: 840px;
    height: 480px;
    background: var(--card);
    border: 1px solid var(--card-edge);
    border-radius: 28px;
    box-shadow: 0 18px 40px rgba(0, 0, 0, 0.55);
    display: flex;
    flex-direction: column;
    align-items: center;
    justify-content: center;
    text-align: center;
    font-family: "Tinos", "Times New Roman", serif;
    color: var(--gold);
  }
  .card--back { height: 360px; }
  .brand-name {
    font-weight: 700;
    font-size: 62px;
    line-height: 1;
    letter-spacing: 1px;
    color: var(--gold);
  }
  .brand-tagline {
    margin-top: 10px;
    font-size: 22px;
    font-weight: 400;
    letter-spacing: 11px;
    color: var(--gold);
  }
  .contact {
    margin-top: 44px;
    display: flex;
    flex-direction: column;
    align-items: center;
    color: var(--gold-soft);
  }
  .contact__name { font-size: 32px; }
  .contact__role { font-size: 26px; margin-top: 4px; }
  .contact__rule {
    width: 22px;
    height: 2px;
    background: var(--gold-soft);
    margin: 14px 0 12px;
  }
  .contact__lines { font-size: 24px; }
</style>
</head>
<body>
  <main class="canvas">
    <section class="card card--back">
      <div class="brand-name">Silver Meridian</div>
      <div class="brand-tagline">Medical grade cannabis</div>
    </section>

    <section class="card card--front">
      <div class="brand-name">Silver Meridian</div>
      <div class="brand-tagline">Medical grade cannabis</div>
      <div class="contact">
        <div class="contact__name">Ron Ben-Amit</div>
        <div class="contact__role">Founder and CEO</div>
        <div class="contact__rule"></div>
        <div class="contact__lines">E: ronbenamit@mailpost-example.com &bull; P: 972-52-3186407</div>
      </div>
    </section>
  </main>
</body>
</html>
```